Business Card Design

Selling Televisions, Velorin, Kavo, Drelvatek, Morenzi
The latest models, sizes ranging from 22"- 75"
Surround Sounds, Sound Bars and Wall Mounts

Target Market(s)

Mainly males/boys/blokes etc

Industry/Entity Type

Business

Contact Information for Business Card

Glen Rudd
07812459306
glrudd@quillnetmail.com

Requirements
Must have
• simplistic design, probably just 2 of the images used

clarity essential
Nice to have
• Metallic if possible

```html
<!DOCTYPE html>
<html lang="en">
<head>
<meta charset="utf-8">
<title>Glen Rudd – Business Card</title>
<link rel="stylesheet" href="https://fonts.googleapis.com/css2?family=Old+Standard+TT:wght@400&family=Open+Sans:wght@400&display=swap">
<style>
  :root {
    --page-bg: #1c1c1c;
    --metal-light: #e4e5e7;
    --metal-mid: #c3c5c8;
    --metal-dark: #9ea1a5;
    --ink: #1f1f1f;
    --name-fill: #cfd1d4;
    --sunset-top: #b7a3c4;
    --sunset-bottom: #2f3538;
    --city-top: #3a4d8f;
    --city-bottom: #c98a3e;
    --bezel: #3b3d40;
  }
  * { box-sizing: border-box; margin: 0; padding: 0; }
  html, body {
    width: 1200px;
    height: 944px;
    overflow: hidden;
    background: var(--page-bg);
  }
  .card {
    position: absolute;
    left: 150px;
    top: 215px;
    width: 900px;
    height: 514px;
    border-radius: 4px;
    background:
      repeating-linear-gradient(0deg, rgba(255,255,255,0.06) 0 1px, rgba(0,0,0,0.03) 1px 3px),
      radial-gradient(ellipse at 55% 40%, var(--metal-light) 0%, var(--metal-mid) 55%, var(--metal-dark) 100%);
    box-shadow: 0 18px 40px rgba(0,0,0,0.6);
  }
  .product-shot {
    position: absolute;
    border: 6px solid var(--bezel);
    border-radius: 3px;
    box-shadow: 0 6px 14px rgba(0,0,0,0.35);
  }
  .product-shot--sunset {
    left: 80px;
    top: 110px;
    width: 270px;
    height: 145px;
    background: linear-gradient(180deg, var(--sunset-top) 0%, #8d8fa6 45%, var(--sunset-bottom) 100%);
  }
  .product-shot--city {
    left: 110px;
    top: 285px;
    width: 270px;
    height: 150px;
    background: linear-gradient(180deg, var(--city-top) 0%, #5a5f8a 40%, var(--city-bottom) 100%);
  }
  .details {
    position: absolute;
    left: 430px;
    top: 150px;
    width: 420px;
    text-align: center;
  }
  .details__name {
    font-family: "Old Standard TT", serif;
    font-size: 58px;
    font-weight: 400;
    letter-spacing: 2px;
    color: var(--name-fill);
    -webkit-text-stroke: 1.4px var(--ink);
    margin-bottom: 18px;
  }
  .details__line {
    font-family: "Open Sans", sans-serif;
    font-size: 22px;
    color: var(--ink);
    line-height: 1.6;
  }
</style>
</head>
<body>
  <div class="card">
    <div class="product-shot product-shot--sunset" role="img" aria-label="Flat-screen television showing a lake at sunset"></div>
    <div class="product-shot product-shot--city" role="img" aria-label="Curved television showing a city skyline at dusk"></div>
    <div class="details">
      <h1 class="details__name">Glen Rudd</h1>
      <p class="details__line">P: 07812459306</p>
      <p class="details__line">E: glrudd@quillnetmail.com</p>
    </div>
  </div>
</body>
</html>
```